New Business Card Design Project

Want a simple but attention grabbing business card. Back Side having mainly our logo and basic info-the front side a typical business card.

Contact Information for Business Card

Hearth & Basin Works
218 NW Larkfield Rd. Suite 207
Marlow Falls, Iowa 50398

phone- 515.284.7093

website is -hbwplains.com

```html
<!DOCTYPE html>
<html lang="en">
<head>
<meta charset="utf-8">
<title>Hearth &amp; Basin Works — Business Card</title>
<link href="https://fonts.googleapis.com/css2?family=Lato:wght@400;700&display=swap" rel="stylesheet">
<style>
  :root {
    --page-bg: #ffffff;
    --brand-blue: #0324fb;
    --ink-blue: #2c7cf3;
    --accent-orange: #ff3511;
    --card-white: #ffffff;
    --card-shadow: rgba(0, 0, 0, 0.22);
  }
  * { margin: 0; padding: 0; box-sizing: border-box; }
  html, body {
    width: 1200px;
    height: 1000px;
    overflow: hidden;
    background: var(--page-bg);
    font-family: "Lato", sans-serif;
  }
  .canvas {
    position: relative;
    width: 1200px;
    height: 1000px;
  }
  .card {
    position: absolute;
    left: 222px;
    width: 757px;
    height: 433px;
    box-shadow: 2px 4px 8px var(--card-shadow);
    overflow: hidden;
  }
  .card--back {
    top: 46px;
    background: var(--brand-blue);
    display: flex;
    align-items: center;
    justify-content: center;
  }
  .card--back .brand-name {
    color: var(--accent-orange);
    font-weight: 700;
    font-size: 50px;
    letter-spacing: 0.5px;
    margin-top: -10px;
  }
  .card--front {
    top: 523px;
    background: var(--card-white);
  }
  .accent-stripe {
    position: absolute;
    right: 0;
    top: 0;
    width: 27px;
    height: 100%;
    background: var(--accent-orange);
  }
  .front-brand {
    position: absolute;
    left: 202px;
    top: 214px;
    transform: translate(-50%, -50%);
    white-space: nowrap;
    color: var(--ink-blue);
    font-weight: 700;
    font-size: 29px;
  }
  .contact {
    position: absolute;
    right: 54px;
    text-align: right;
    color: var(--ink-blue);
    white-space: nowrap;
    line-height: 1;
  }
  .contact__name {
    top: 108px;
    font-size: 32px;
    font-weight: 700;
  }
  .contact__title {
    top: 144px;
    font-size: 17px;
  }
  .divider {
    position: absolute;
    left: 405px;
    right: 27px;
    top: 176px;
    height: 3px;
    background: var(--accent-orange);
  }
  .contact__phone {
    top: 196px;
    font-size: 34px;
    font-weight: 700;
  }
  .contact__address {
    top: 247px;
    font-size: 20px;
    line-height: 25px;
  }
  .contact__web {
    top: 314px;
    font-size: 19px;
  }
</style>
</head>
<body>
  <main class="canvas">
    <section class="card card--back" aria-label="Card back">
      <div class="brand-name">Hearth &amp; Basin Works</div>
    </section>

    <section class="card card--front" aria-label="Card front">
      <div class="front-brand">Hearth &amp; Basin Works</div>

      <div class="contact contact__name">Example Name</div>
      <div class="contact contact__title">Director</div>
      <div class="divider"></div>
      <div class="contact contact__phone">515.284.7093</div>
      <div class="contact contact__address">218 NW Larkfield Rd. Suite 207<br>Marlow Falls, Iowa 50398</div>
      <div class="contact contact__web">www.hbwplains.com</div>

      <div class="accent-stripe"></div>
    </section>
  </main>
</body>
</html>
```